Web Site Design

We need to design the whole web site for our small start up. We sell hospitality and culinary art internships abroad. I did my own design with WIX which is horrible meanwhile I started with my business. You can see it www.brightvoyage-intern.example I will need you to create a new and attractive web site and to leave it working on wix. The internship destinations are United Arab Emirates, Thailand, China, Spain, Brazil and maybe leave a couple of pages for future destinations.You could also get other ideas of other sites that do internships.

Target Market(s)

Students and recent graduates of hospitality and culinary art majors

Industry/Entity Type

Education

Number of Pages Required

5+ page

Requirements
Must have
• Addittional to our program destinations, or to the pages in the current site. The website must contain a page for Universities or Hotels who require our service

```html
<!DOCTYPE html>
<html lang="en">
<head>
<meta charset="utf-8">
<title>China Hospitality Internships – Bright Voyage</title>
<link rel="stylesheet" href="https://fonts.googleapis.com/css2?family=Albert+Sans:wght@400;600;700&family=Playfair+Display:wght@400;700&display=swap">
<style>
:root{
  --ink:#111111;
  --partner-ink:#2a2a2a;
  --white:#ffffff;
  --nav-dim:#d8d8d8;
  --teal:#1f8a8c;
  --teal-dark:#176f72;
  --footer:#2f2f2f;
  --footer-text:#f2f2f2;
  --hero-top:#5c6a78;
  --hero-mid:#b8a68a;
  --hero-low:#7d6a55;
  --photo-sky:#6fa7d6;
  --photo-pool:#57b6d3;
  --photo-grass:#6f9a3c;
}
*{box-sizing:border-box;margin:0;padding:0}
html,body{width:1200px;height:2890px;overflow:hidden;background:var(--white)}
body{position:relative;font-family:"Albert Sans",Arial,sans-serif;color:var(--ink)}

.hero{position:absolute;left:0;top:0;width:1200px;height:602px;
  background:linear-gradient(180deg,var(--hero-top) 0%,#8f94a0 22%,var(--hero-mid) 55%,var(--hero-low) 100%)}
.site-nav{position:absolute;left:0;top:0;width:1200px;height:110px}
.brand{position:absolute;left:100px;top:25px;display:flex;align-items:center;gap:14px;color:var(--white);
  font-family:"Playfair Display",Georgia,serif;font-weight:700;font-size:18px;line-height:1.1;text-transform:uppercase}
.brand-dot{width:56px;height:56px;border-radius:50%;border:3px solid var(--white)}
.nav-links{position:absolute;top:45px;left:353px;display:flex;list-style:none;font-family:"Playfair Display",Georgia,serif;font-weight:700;font-size:12px;letter-spacing:.2px;text-transform:uppercase}
.nav-links li{color:var(--white)}
.nav-links li:first-child{color:var(--nav-dim);font-weight:400}
.nav-links li:nth-child(1){width:114px}
.nav-links li:nth-child(2){width:94px}
.nav-links li:nth-child(3){width:118px}
.hero-title{position:absolute;left:86px;top:240px;color:var(--white);font-family:"Playfair Display",Georgia,serif;font-weight:700;font-size:104px;line-height:1}

.intro{position:absolute;left:116px;top:654px;width:975px;font-size:30px;line-height:42.5px}
.intro p+p{margin-top:42.5px}

.details{position:absolute;left:100px;top:1108px;width:1000px;font-size:30px;line-height:42.5px}
.details h2{font-size:34px;font-weight:700;line-height:46px}
.details ul{list-style:none}
.positions,.period{width:540px}
.period{margin-top:8px}
.benefits{margin-top:10px;width:950px}
.benefits li{padding-left:16px;text-indent:-16px}
.benefits strong{font-weight:700}
.photo{position:absolute;left:658px;top:1123px;width:428px;height:474px;
  background:linear-gradient(180deg,var(--photo-sky) 0%,#a9c9e6 25%,#c9a978 42%,var(--photo-pool) 58%,var(--photo-grass) 82%,#4e7a2a 100%)}

.partners{position:absolute;left:87px;top:2117px;width:1013px}
.partners h2{font-size:32px;font-weight:700;line-height:44px;margin-left:11px}
.partner-grid{margin-top:60px;display:grid;grid-template-columns:repeat(5,1fr);row-gap:35px}
.partner{height:110px;display:flex;align-items:center;justify-content:center;font-size:24px;font-weight:600;color:var(--partner-ink);text-align:center;line-height:1.15}

.cta{position:absolute;left:467px;top:2502px;width:228px;height:66px;border-radius:4px;background:linear-gradient(180deg,var(--teal),var(--teal-dark));
  color:var(--white);font-family:"Playfair Display",Georgia,serif;font-weight:700;font-size:29px;display:flex;align-items:center;justify-content:center;text-decoration:none}

.site-footer{position:absolute;left:0;top:2595px;width:1200px;height:295px;background:var(--footer);color:var(--footer-text);font-size:21px;line-height:31px}
.footer-col{position:absolute;top:22px}
.footer-col h3{font-size:22px;font-weight:700;line-height:31px}
.footer-col ul{list-style:none}
.col-destinations{left:106px}
.col-programs{left:307px}
.col-how{left:533px}
.col-contact{left:739px}
.contact-list li{display:flex;align-items:center;gap:16px;height:47px}
.contact-list li.email{height:34px}
.flag{width:30px;height:30px;border-radius:50%;flex:none}
.flag-us{background:linear-gradient(180deg,#b22234 0 50%,#3c3b6e 50%)}
.flag-eu{background:#1f49a8}
.flag-au{background:#1a2f8a}
.flag-mx{background:linear-gradient(90deg,#0b7a3e 0 33%,#ffffff 33% 66%,#c8102e 66%)}
.social{position:absolute;left:102px;top:214px;display:flex;gap:16px;list-style:none}
.social li{width:38px;height:38px;border-radius:50%;background:var(--footer-text)}
</style>
</head>
<body>

<header class="hero" role="img" aria-label="Photograph of a round tiered temple hall above a wide stone staircase with white marble balustrades under a cloudy sky">
  <nav class="site-nav">
    <div class="brand"><span class="brand-dot"></span><span>Bright<br>Voyage</span></div>
    <ul class="nav-links">
      <li>Destinations</li>
      <li>Programs</li>
      <li>How it works</li>
      <li>Contact</li>
    </ul>
  </nav>
  <h1 class="hero-title">China</h1>
</header>

<section class="intro">
  <p>Hospitality internships are mainly designed for professionals and students in their final university semesters who are looking to learn the ways of working in the growing Chinese market's hospitality industry.</p>
  <p>The hotels where participants carry out their internships are 4 – 5 star Chinese and international hotels or luxury boutique properties. The program will take place in the most important tourist cities in China, chief among them are Shanghai, which is the Financial Center and the most modern and cosmopolitan city of China and Beijing, which is the cultural and political center of this great country.</p>
</section>

<section class="details">
  <div class="positions">
    <h2>Possible positions include</h2>
    <ul>
      <li>-Food &amp; Beverage</li>
      <li>-Guest Services</li>
      <li>-Front Desk</li>
      <li>-Manager in Training</li>
      <li>-... more!</li>
    </ul>
  </div>
  <div class="period">
    <h2>Period</h2>
    <ul><li>-6 months</li></ul>
  </div>
  <div class="benefits">
    <h2>Benefit package</h2>
    <ul>
      <li>-<strong>Guaranteed</strong> position. We<br>guarantee that we will find a position<br>for you based on your experience,<br>goals, and availability...or <strong>your money back.</strong></li>
      <li>-Monthly Stippen US$ 400.</li>
      <li>-Free accommodation provided by the hotel either inside the actual<br>hotel or in an apartment nearby.</li>
      <li>-Working meals.</li>
      <li>-Wanderfolio guide.</li>
      <li>-Airport pickup.</li>
      <li>-Invitation Letter for visa procedure.</li>
      <li>-US$ 1500 Scholarship to study Chinese with our partner school during<br>your internship program.</li>
    </ul>
  </div>
</section>

<div class="photo" role="img" aria-label="Photograph of a thatched parasol and two white lounge chairs beside a round pool on green lawn"></div>

<section class="partners">
  <h2>Previous interns have secured positions at</h2>
  <div class="partner-grid">
    <div class="partner">Larkspur Hotels</div>
    <div class="partner">Amberly Suites</div>
    <div class="partner">Norwyn House</div>
    <div class="partner">Calloway Resorts</div>
    <div class="partner">Tidewater Grand</div>
    <div class="partner">Pinecrest Hotels</div>
    <div class="partner">Ostara Retreats</div>
    <div class="partner">Meridale Inn</div>
    <div class="partner">Fenwick Hall</div>
    <div class="partner">Brookhaven Lodge</div>
  </div>
</section>

<a class="cta" href="#">Get started</a>

<footer class="site-footer">
  <div class="footer-col col-destinations">
    <h3>Destinations</h3>
    <ul><li>Spain</li><li>France</li><li>China</li></ul>
  </div>
  <div class="footer-col col-programs">
    <h3>Programs</h3>
    <ul><li>Culinary</li><li>Food &amp; Beverage</li><li>Front office</li><li>Guest relations</li></ul>
  </div>
  <div class="footer-col col-how">
    <h3>How it works</h3>
    <ul><li>Apply</li><li>Deposit</li><li>Interview</li><li>Placement</li><li>Payment</li><li>Visa</li></ul>
  </div>
  <div class="footer-col col-contact">
    <h3>Contact</h3>
    <ul class="contact-list">
      <li class="email">Email info@brightvoyage-intern.example</li>
      <li><span class="flag flag-us"></span>United States +1 555-014-2290</li>
      <li><span class="flag flag-eu"></span>Europe +33 7 0000 1842</li>
      <li><span class="flag flag-au"></span>Australia +61 400 555 017</li>
      <li><span class="flag flag-mx"></span>Mexico +52 55 5550 1836</li>
    </ul>
  </div>
  <ul class="social" aria-label="Social links">
    <li></li><li></li><li></li><li></li><li></li>
  </ul>
</footer>

</body>
</html>
```